Local Flower Farm Needs Business Card Design

I need business cards designed for a flower farm based in Eudora, Kansas.
Business Info:
We are a local cut flower farm located in Eudora, Kansas, founded by Darla Whitcombe. What started as a passion for agriculture and search for more joy in daily life has blossomed into a small business dedicated to providing the community with beautiful, fresh, and sustainable flowers. We specialize in local, seasonal blooms, ensuring that every petal reflects the care and dedication we pour into our craft. Our mission is to deliver the highest quality flowers directly to our customers through local farmers markets and to florists who share our commitment to sustainability. Join us in celebrating the beauty of nature, one bloom at a time!
Contact Details:
Darla Whitcombe
Owner
Phone 913-555-0148
Facebook: Rosalind Pike Gardens
Instagram: @RosalindPikeGardens
Website: RosalindPikeGardens.example
Target Market(s)
Wholesale to Florists and Direct to Consumer via Farmers Market
Industry/Entity Type
Florist, Farm
Contact Information for Business Card
Name, Contact Info, Logo
Look and feel
Each slider illustrates characteristics of the customer's brand and the style your logo design should communicate.

```html
<!DOCTYPE html>
<html lang="en">
<head>
<meta charset="utf-8">
<title>Rosalind Pike Gardens — Business Card</title>
<link rel="stylesheet" href="https://fonts.googleapis.com/css2?family=Montserrat:wght@400;500;700&display=swap">
<style>
  :root {
    --backdrop: #2b2b2b;
    --teal-deep: #0b3437;
    --teal-mid: #0f4649;
    --teal-glow: #4cb3c4;
    --paper: #ffffff;
    --ink: #0d2f31;
    --ink-soft: #3a4a4b;
  }
  * { box-sizing: border-box; margin: 0; padding: 0; }
  html, body { width: 1200px; height: 900px; overflow: hidden; }
  body {
    background: var(--backdrop);
    font-family: "Montserrat", sans-serif;
    position: relative;
  }
  .card {
    position: absolute;
    left: 280px;
    width: 640px;
    height: 366px;
    border-radius: 26px;
    overflow: hidden;
    box-shadow: 0 14px 30px rgba(0,0,0,.45);
  }
  /* back side */
  .card-back { top: 62px; background: var(--teal-deep); }
  .monogram-field {
    position: absolute; inset: 0;
    background:
      linear-gradient(115deg, var(--teal-glow) 0%, #2a7f8c 18%, var(--teal-mid) 42%, var(--teal-deep) 70%, #0a2c2f 100%);
    opacity: .9;
  }
  .back-mark {
    position: absolute;
    left: 430px; top: 150px;
    color: var(--paper);
    font-weight: 700;
    font-size: 17px;
    letter-spacing: .04em;
  }
  /* front side */
  .card-front { top: 472px; background: var(--paper); }
  .holder { position: absolute; left: 44px; top: 56px; }
  .holder-name { font-weight: 700; font-size: 25px; color: var(--ink); }
  .holder-role { font-size: 14px; color: var(--ink-soft); margin-top: 4px; }
  .brand-seal {
    position: absolute; left: 412px; top: 32px;
    width: 200px; height: 200px;
    border: 2px solid var(--ink);
    border-radius: 50%;
    display: flex; align-items: center; justify-content: center;
    text-align: center;
    color: var(--ink);
    font-weight: 700; font-size: 19px; line-height: 1.25;
    padding: 30px;
  }
  .contact-list {
    position: absolute; left: 44px; top: 192px;
    list-style: none;
    font-size: 15px; color: var(--ink);
  }
  .contact-list li { display: flex; align-items: center; gap: 9px; height: 23px; }
  .contact-list svg { width: 13px; height: 13px; flex: none; }
  .wave { position: absolute; left: 0; top: 0; width: 640px; height: 366px; }
</style>
</head>
<body>
  <section class="card card-back">
    <div class="monogram-field" role="img" aria-label="Repeating brand monogram pattern with a soft teal shine"></div>
    <span class="back-mark">Rosalind Pike Gardens</span>
  </section>

  <section class="card card-front">
    <svg class="wave" viewBox="0 0 640 366" aria-hidden="true">
      <path d="M0,292 C190,322 430,292 640,178 L640,366 L0,366 Z" fill="var(--teal-deep)"/>
      <path d="M0,308 C200,338 440,306 640,196" fill="none" stroke="var(--paper)" stroke-width="3"/>
    </svg>

    <div class="holder">
      <p class="holder-name">Darla Whitcombe</p>
      <p class="holder-role">Owner</p>
    </div>

    <div class="brand-seal">Rosalind Pike Gardens</div>

    <ul class="contact-list">
      <li>
        <svg viewBox="0 0 16 16"><path d="M3.5 1.5l2.4 0.2 1 3-1.6 1.2c.8 1.8 2 3 3.8 3.8l1.2-1.6 3 1 .2 2.4c-.2 1-1 1.6-2 1.6C6.6 13 3 9.4 2 4.5c0-1 .6-2.8 1.5-3z" fill="var(--ink)"/></svg>
        913-555-0148
      </li>
      <li>
        <svg viewBox="0 0 16 16"><circle cx="8" cy="8" r="7" fill="var(--ink)"/></svg>
        Rosalind Pike Gardens
      </li>
      <li>
        <svg viewBox="0 0 16 16"><circle cx="8" cy="8" r="7" fill="var(--ink)"/></svg>
        @RosalindPikeGardens
      </li>
      <li>
        <svg viewBox="0 0 16 16"><g fill="none" stroke="var(--ink)" stroke-width="1.6"><circle cx="8" cy="8" r="6.5"/><ellipse cx="8" cy="8" rx="2.8" ry="6.5"/><path d="M1.5 8h13"/></g></svg>
        www.RosalindPikeGardens.example
      </li>
    </ul>
  </section>
</body>
</html>
```